Design for supplement packages

We are developing a new supplement brand are looking for a label, based on the design of our naturopath practice. It should include our logo, the basic colors are green, gold and white. www.haus-solvarin.de is the practices web site.

Target Market(s)

Europe and North America

Industry/Entity Type

Supplement

Font styles to use
Sans Serif

Colors
acd037
ffffff

Requirements
Should not have
• A too busy design. I like it simple and high class

```html
<!DOCTYPE html>
<html lang="en">
<head>
<meta charset="utf-8">
<title>Antioxidant Protection – Supplement Label</title>
<link href="https://fonts.googleapis.com/css2?family=Barlow+Semi+Condensed:wght@500;600;700&family=Barlow:wght@400&display=swap" rel="stylesheet">
<style>
  :root {
    --page-bg: #ecebe8;
    --label-white: #ffffff;
    --ink-grey: #5e6062;
    --brand-taupe: #8f7c6c;
    --band-green: #bfd255;
    --band-green-light: #cfdc7e;
    --band-taupe: #a49384;
    --badge-taupe: #9b8677;
    --accent-pale: #e6ecc8;
    --text-white: #ffffff;
  }
  * { box-sizing: border-box; margin: 0; padding: 0; }
  html, body {
    width: 1200px;
    height: 900px;
    overflow: hidden;
    background: var(--page-bg);
  }
  .canvas {
    position: relative;
    width: 1200px;
    height: 900px;
  }
  .label {
    position: absolute;
    left: 250px;
    top: 30px;
    width: 700px;
    height: 840px;
    background: var(--label-white);
    overflow: hidden;
    box-shadow: 0 6px 24px rgba(60, 50, 40, 0.12);
  }
  .label__decor {
    position: absolute;
    right: 0;
    top: 0;
    width: 230px;
    height: 700px;
    background: linear-gradient(100deg, rgba(230,236,200,0) 0%, rgba(230,236,200,0.75) 55%, rgba(214,224,170,0.8) 100%);
  }
  .brand {
    position: absolute;
    left: 52px;
    top: 62px;
    display: flex;
    align-items: center;
    gap: 18px;
  }
  .brand__mark {
    width: 46px;
    height: 46px;
    border-radius: 50%;
    background: var(--band-green);
  }
  .brand__name {
    font-family: "Barlow", sans-serif;
    font-weight: 400;
    font-size: 52px;
    letter-spacing: 1px;
    color: var(--brand-taupe);
  }
  .product-title {
    position: absolute;
    left: 52px;
    top: 262px;
    font-family: "Barlow Semi Condensed", sans-serif;
    font-weight: 600;
    font-size: 104px;
    line-height: 100px;
    color: var(--ink-grey);
    letter-spacing: 1px;
  }
  .benefits {
    position: absolute;
    left: 0;
    top: 510px;
    width: 100%;
    height: 210px;
    background: linear-gradient(90deg, var(--band-green) 0%, var(--band-green) 60%, var(--band-green-light) 100%);
    padding: 26px 0 0 54px;
    list-style: none;
  }
  .benefits__item {
    display: flex;
    align-items: center;
    gap: 10px;
    font-family: "Barlow Semi Condensed", sans-serif;
    font-weight: 600;
    font-size: 38px;
    line-height: 56px;
    color: var(--text-white);
  }
  .benefits__icon { width: 20px; height: 20px; flex: none; }
  .footer-band {
    position: absolute;
    left: 0;
    top: 720px;
    width: 100%;
    height: 120px;
    background: var(--band-taupe);
    padding: 30px 0 0 54px;
    font-family: "Barlow Semi Condensed", sans-serif;
    font-weight: 700;
    font-size: 44px;
    letter-spacing: 1px;
    color: var(--text-white);
  }
  .count-badge {
    position: absolute;
    left: 555px;
    top: 610px;
    width: 210px;
    height: 210px;
    border-radius: 50%;
    background: var(--badge-taupe);
    font-family: "Barlow Semi Condensed", sans-serif;
    color: var(--text-white);
    text-align: left;
    padding: 26px 0 0 44px;
  }
  .count-badge__number {
    display: block;
    font-weight: 700;
    font-size: 84px;
    line-height: 84px;
  }
  .count-badge__unit {
    display: block;
    font-weight: 500;
    font-size: 28px;
    letter-spacing: 1px;
    margin-left: -18px;
  }
</style>
</head>
<body>
<main class="canvas">
  <section class="label">
    <div class="label__decor" role="img" aria-label="Soft pale green organic background shapes"></div>

    <div class="brand">
      <span class="brand__mark"></span>
      <span class="brand__name">Haus Solvarin</span>
    </div>

    <h1 class="product-title">ANTIOXIDANT<br>PROTECTION</h1>

    <ul class="benefits">
      <li class="benefits__item">
        <svg class="benefits__icon" viewBox="0 0 20 20"><circle cx="10" cy="10" r="8.5" fill="none" stroke="#fff" stroke-width="2"/><path d="M6 10.5l3 3 5-6" fill="none" stroke="#fff" stroke-width="2" stroke-linecap="round" stroke-linejoin="round"/></svg>
        Support brain functions
      </li>
      <li class="benefits__item">
        <svg class="benefits__icon" viewBox="0 0 20 20"><circle cx="10" cy="10" r="8.5" fill="none" stroke="#fff" stroke-width="2"/><path d="M6 10.5l3 3 5-6" fill="none" stroke="#fff" stroke-width="2" stroke-linecap="round" stroke-linejoin="round"/></svg>
        Support memory
      </li>
      <li class="benefits__item">
        <svg class="benefits__icon" viewBox="0 0 20 20"><circle cx="10" cy="10" r="8.5" fill="none" stroke="#fff" stroke-width="2"/><path d="M6 10.5l3 3 5-6" fill="none" stroke="#fff" stroke-width="2" stroke-linecap="round" stroke-linejoin="round"/></svg>
        Support health circulation
      </li>
    </ul>

    <div class="footer-band">DIETARY SUPPLEMENT</div>

    <div class="count-badge">
      <span class="count-badge__number">90</span>
      <span class="count-badge__unit">CAPSULES</span>
    </div>
  </section>
</main>
</body>
</html>
```